New business needs a slick but classy, conservative and elegant Legal Letterhead

We need a new letterhead for a law firm that is slick but very classy and also understated.

The name of the firm is K.L. Marlow Lawyers.

All information about the Law firm should appear at the top of the page. Please no firm information in the footer.

It should have a clean, neat look. No watermarks or bold graphics please.

Info should include the name of the law firm, both the street address and postal address, the phone number and the fax number, the names of the principals, the website. We have attached a word document that contains the relevant information.

We have attached a copy of the business card for further information purposes.

We also need a law society logo to appear (probably on the bottom right hand side of the letterhead?) that states our affiliation to the law society. It is attached and must not be altered in any way. It can be small.

The only footer text we require is as worded in the attached information document.

We would like to see designs that use red and white - in an understated, elegant style - not too modern or too gaudy looking.

The final design should communicate that we mean business and that we are to be trusted.
Updates

Please insert firm's name K.L. Marlow Lawyers on letterhead! I have removed KLM logo as designers were using it instead of the name of the firm. Thank you!

Industry/Entity Type

Legal

Font styles to use
Serif

Colors
ec1f27
ffffff

Requirements
Must have
• All information contained in the word document attached - firm details, law society affiliation logo, firm name & firm logo, principals' names.
Should not have
• watermarks
• no firm details in footer

```html
<!DOCTYPE html>
<html lang="en">
<head>
<meta charset="utf-8">
<title>K.L. Marlow Lawyers — Stationery Set</title>
<link href="https://fonts.googleapis.com/css2?family=Libre+Baskerville:wght@400;700&display=swap" rel="stylesheet">
<style>
:root{
  --red:#ec1f27;
  --white:#ffffff;
  --ink:#4a4a4a;
  --edge:#c9c9c9;
  --fold:#e4e4e4;
}
*{margin:0;padding:0;box-sizing:border-box}
html,body{width:863px;height:1200px;overflow:hidden;background:var(--white)}
body{position:relative;font-family:"Libre Baskerville",Georgia,serif;color:var(--ink)}
.sheet{position:absolute;background:var(--white);border:1px solid var(--edge)}
.mark{font-family:"Libre Baskerville",Georgia,serif;font-weight:700;color:var(--white);letter-spacing:2px;text-align:center}
.details{font-size:8px;line-height:1.55}
.details p{margin-bottom:6px}
.icon-row{display:flex;align-items:center;gap:4px}
.icon-row svg{width:8px;height:8px;flex:none}

/* Letterhead */
.letterhead{left:2px;top:0;width:558px;height:675px}
.letterhead .band{position:absolute;left:0;top:0;width:100%;height:34px;background:var(--red)}
.letterhead .brand{position:absolute;left:395px;top:14px;width:140px;height:90px;background:var(--red);display:flex;flex-direction:column;align-items:center;justify-content:center}
.letterhead .brand .mark{font-size:34px}
.letterhead .brand .firm{font-size:7px;color:var(--white);letter-spacing:1px;margin-top:4px}
.letterhead .details{position:absolute;left:408px;top:115px}
.letterhead .principals{position:absolute;left:40px;top:486px;font-size:8px;line-height:1.5}
.letterhead .principals .name{color:var(--red)}
.letterhead .footer{position:absolute;left:0;top:637px;width:100%;height:20px;background:var(--red);color:var(--white);font-size:9px;display:flex;align-items:center;justify-content:center}
.letterhead .footer-rule{position:absolute;left:0;top:662px;width:100%;height:3px;background:var(--red)}

/* Business card */
.card{left:590px;top:0;width:268px;height:330px}
.card .top{position:absolute;left:0;top:0;width:100%;height:125px;background:var(--red);display:flex;flex-direction:column;align-items:center;justify-content:center}
.card .top .mark{font-size:36px}
.card .top .firm{font-size:7px;color:var(--white);letter-spacing:1px;margin-top:4px}
.card .details{position:absolute;left:22px;top:140px;font-size:7.5px}
.card .person{position:absolute;right:18px;top:300px;font-size:7.5px;color:var(--red)}

/* Envelopes */
.envelope{left:14px;width:546px}
.env-back{top:690px;height:232px}
.env-front{top:935px;height:258px}
.envelope svg.flap{position:absolute;left:0;top:0;width:100%;height:100%}
.env-back .mark{position:absolute;left:223px;top:18px;width:100px;font-size:30px}
.env-back .firm{position:absolute;left:223px;top:58px;width:100px;text-align:center;font-size:6px;color:var(--white);letter-spacing:1px}
.env-front .return{position:absolute;left:14px;top:58px}
.env-front .return .mark{color:var(--red);font-size:18px;text-align:left;letter-spacing:1px}
.env-front .return .details{font-size:5.5px;line-height:1.5;margin-top:4px}
</style>
</head>
<body>

<section class="sheet letterhead" aria-label="Letterhead">
  <div class="band"></div>
  <div class="brand"><div class="mark">KLM</div><div class="firm">LAWYERS</div></div>
  <div class="details">
    <p>Shop 4, 18-20 Elmwood Parade<br>Harlow Vale NSW 2299</p>
    <p>PO Box 7716<br>Harlow Vale NSW 2299</p>
    <div class="icon-row"><svg viewBox="0 0 10 10"><path d="M2 1h2l1 2-1.5 1a6 6 0 0 0 2.5 2.5L7 5l2 1v2a1 1 0 0 1-1 1A8 8 0 0 1 1 2a1 1 0 0 1 1-1z" fill="#4a4a4a"/></svg>(02) 9150 2418</div>
    <div class="icon-row"><svg viewBox="0 0 10 10"><rect x="1" y="3" width="8" height="5" fill="#4a4a4a"/><rect x="3" y="1" width="4" height="2" fill="#4a4a4a"/></svg>(02) 9150 2419</div>
    <div class="icon-row"><svg viewBox="0 0 10 10"><circle cx="5" cy="5" r="4" fill="none" stroke="#4a4a4a"/><path d="M1 5h8M5 1v8" stroke="#4a4a4a" stroke-width=".7"/></svg>www.klmarlow.com.au</div>
  </div>
  <div class="principals">Principals<br><span class="name">Kathryn L. Marlow</span></div>
  <div class="footer">Liability limited by a scheme approved under Professional Standards Legislation</div>
  <div class="footer-rule"></div>
</section>

<section class="sheet card" aria-label="Business card">
  <div class="top"><div class="mark">KLM</div><div class="firm">LAWYERS</div></div>
  <div class="details">
    <p>Shop 4, 18-20 Elmwood Parade<br>Harlow Vale NSW 2299</p>
    <p>PO Box 7716<br>Harlow Vale NSW 2299</p>
    <div class="icon-row"><svg viewBox="0 0 10 10"><path d="M2 1h2l1 2-1.5 1a6 6 0 0 0 2.5 2.5L7 5l2 1v2a1 1 0 0 1-1 1A8 8 0 0 1 1 2a1 1 0 0 1 1-1z" fill="#4a4a4a"/></svg>(02) 9150 2418</div>
    <div class="icon-row"><svg viewBox="0 0 10 10"><rect x="1" y="3" width="8" height="5" fill="#4a4a4a"/><rect x="3" y="1" width="4" height="2" fill="#4a4a4a"/></svg>(02) 9150 2419</div>
    <div class="icon-row"><svg viewBox="0 0 10 10"><circle cx="5" cy="5" r="4" fill="none" stroke="#4a4a4a"/><path d="M1 5h8M5 1v8" stroke="#4a4a4a" stroke-width=".7"/></svg>www.klmarlow.com.au</div>
  </div>
  <div class="person">Kathryn L. Marlow, Principal</div>
</section>

<section class="sheet envelope env-back" aria-label="Envelope back">
  <svg class="flap" viewBox="0 0 546 232" preserveAspectRatio="none">
    <path d="M0 232L220 120M546 232L326 120" stroke="var(--fold)" stroke-width="1.5" fill="none"/>
    <polygon points="0,0 546,0 546,8 273,128 0,8" fill="var(--red)"/>
  </svg>
  <div class="mark">KLM</div>
  <div class="firm">LAWYERS</div>
</section>

<section class="sheet envelope env-front" aria-label="Envelope front">
  <svg class="flap" viewBox="0 0 546 258" preserveAspectRatio="none">
    <polygon points="0,0 546,0 546,36 273,44 0,36" fill="var(--red)"/>
  </svg>
  <div class="return">
    <div class="mark">KLM</div>
    <div class="details">Shop 4, 18-20 Elmwood Parade<br>Harlow Vale NSW 2299<br>PO Box 7716<br>www.klmarlow.com.au</div>
  </div>
</section>

</body>
</html>
```